Smile club flyer design

I am launching an office smile club and would like a design that sits my branding and that is appealing to customers. I have a design (I need a new one) that has all the information.
My website is maplecrestdentalcaretn.example
Brand color is green. The design can be any color

Target Market(s)

Ages 30+

Industry/Entity Type

Dental

Font styles to use
Serif

Requirements
Must have
• Appealing to patients

```html
<!DOCTYPE html>
<html lang="en">
<head>
<meta charset="utf-8">
<title>Maplecrest Dental Care – Smile Club Membership Flyer</title>
<link rel="stylesheet" href="https://fonts.googleapis.com/css2?family=Allura&family=Josefin+Sans:wght@300;400;600;700&family=Montserrat:wght@300;400;800;900&family=Righteous&display=swap">
<style>
  :root{
    --bg:#eef0ee;
    --mint-1:#bff1e6;
    --mint-2:#e3faf6;
    --mint-blob:#86e9d3;
    --brand-green:#1c9a4f;
    --deep-green:#0d5a37;
    --ink:#1f3b30;
    --card-pink:#fde5e7;
    --sage:#6f9480;
    --sage-dark:#4e7260;
    --peach:#e9a872;
    --peach-dark:#c98a55;
    --gray-green:#8ea79a;
    --white:#ffffff;
  }
  *{box-sizing:border-box;margin:0;padding:0}
  html,body{width:1200px;height:1200px;overflow:hidden;background:var(--bg)}
  .flyer{
    position:absolute;left:160px;top:40px;width:880px;height:1120px;overflow:hidden;
    background:linear-gradient(160deg,var(--mint-1) 0%,var(--mint-2) 55%,var(--mint-1) 100%);
    box-shadow:0 8px 24px rgba(0,0,0,.12);
    font-family:"Josefin Sans",sans-serif;color:var(--ink);
  }
  .backdrop{position:absolute;inset:0}
  .abs{position:absolute}
  .brand{left:0;right:0;top:48px;text-align:center;font-family:"Josefin Sans",sans-serif;font-weight:700;font-size:40px;color:var(--deep-green);letter-spacing:1px}
  .intro{left:0;right:0;top:130px;text-align:center;font-family:"Allura",cursive;font-size:70px;color:var(--deep-green);line-height:1}
  .headline{left:0;right:0;top:215px;text-align:center;font-family:"Montserrat",sans-serif;font-weight:900;font-size:92px;letter-spacing:3px;color:var(--brand-green);line-height:1}
  .subhead{left:0;right:0;top:308px;text-align:center;font-family:"Montserrat",sans-serif;font-weight:300;font-size:54px;color:var(--deep-green);line-height:1;letter-spacing:1px}
  .tagline{left:90px;top:375px;font-family:"Montserrat",sans-serif;font-weight:400;font-size:23px;color:var(--deep-green)}
  .tagline strong{font-weight:800}

  .plan{position:absolute;top:428px;width:232px;height:330px;background:var(--card-pink);border-radius:14px 14px 90px 6px;box-shadow:3px 5px 10px rgba(0,0,0,.12)}
  .plan--core{left:70px}
  .plan--bright{left:335px}
  .plan--total{left:600px}
  .ribbon{position:absolute;left:-18px;top:20px;width:215px;height:54px;padding:8px 0 0 34px;color:var(--white);border-radius:0 4px 4px 0}
  .ribbon::after{content:"";position:absolute;left:0;bottom:-14px;border-top:14px solid rgba(0,0,0,.35);border-left:18px solid transparent}
  .plan--core .ribbon{background:var(--sage)}
  .plan--bright .ribbon{background:var(--peach)}
  .plan--total .ribbon{background:var(--gray-green)}
  .ribbon__name{display:block;font-family:"Montserrat",sans-serif;font-weight:800;font-size:24px;line-height:1}
  .ribbon__type{display:block;font-family:"Montserrat",sans-serif;font-weight:400;font-size:16px;line-height:1.1}
  .price{position:absolute;left:0;right:0;top:84px;text-align:center;color:var(--deep-green);padding-bottom:10px;margin:0 18px;border-bottom:1px solid rgba(31,59,48,.2)}
  .plan--bright .price{color:var(--peach-dark)}
  .price sup{font-family:"Righteous",sans-serif;font-size:18px;vertical-align:top;position:relative;top:4px}
  .price b{font-family:"Righteous",sans-serif;font-weight:400;font-size:40px;letter-spacing:1px}
  .price small{font-family:"Montserrat",sans-serif;font-size:13px;font-weight:400}
  .features{position:absolute;left:18px;right:14px;top:150px;list-style:none}
  .features li{display:flex;gap:7px;font-size:14px;line-height:1.3;margin-bottom:16px;color:var(--ink)}
  .tick{flex:0 0 13px;width:13px;height:13px;margin-top:1px}

  .package{position:absolute;left:60px;top:790px;width:400px;height:195px;background:var(--card-pink);border-radius:20px 60px 90px 6px;box-shadow:3px 5px 10px rgba(0,0,0,.12)}
  .package .ribbon{top:20px;width:230px;background:var(--peach)}
  .package .features{top:95px;left:36px;right:160px}
  .badge-new{position:absolute;right:40px;top:30px;font-family:"Montserrat",sans-serif;font-weight:900;font-size:32px;color:var(--sage-dark)}
  .package-price{position:absolute;right:38px;top:88px;color:var(--peach-dark)}
  .package-price sup{font-family:"Righteous",sans-serif;font-size:24px;vertical-align:top}
  .package-price b{font-family:"Righteous",sans-serif;font-weight:400;font-size:56px}

  .financing{position:absolute;left:480px;top:815px;width:380px}
  .financing__title{font-family:"Montserrat",sans-serif;font-size:19px;color:var(--deep-green)}
  .partners{display:flex;align-items:center;gap:26px;margin-top:14px}
  .partner{display:flex;align-items:center;gap:7px;font-family:"Josefin Sans",sans-serif;font-weight:700;font-size:28px}
  .partner--a{color:var(--deep-green)}
  .partner--b{color:#8a2f2f}
  .partner i{display:block;width:16px;height:16px;border-radius:50%;background:currentColor}
  .financing__note{margin-top:22px;font-family:"Montserrat",sans-serif;font-size:14px;color:var(--deep-green);line-height:1.35}
  .financing__note span{display:block;font-family:"Josefin Sans",sans-serif;font-size:13px}

  .cta{left:0;right:0;top:1040px;text-align:center;font-family:"Montserrat",sans-serif;font-weight:900;font-size:35px;color:var(--deep-green);letter-spacing:.5px}
</style>
</head>
<body>
<main class="flyer">
  <svg class="backdrop" viewBox="0 0 880 1120" aria-hidden="true">
    <path d="M0 0 H150 C60 40 60 120 110 170 C170 230 150 300 60 300 C30 300 10 290 0 285 Z" fill="var(--mint-blob)" opacity=".7"/>
    <path d="M880 0 V170 C820 120 760 60 720 0 Z" fill="var(--mint-blob)" opacity=".35"/>
    <path d="M0 300 C20 340 30 420 0 470 Z" fill="var(--white)" opacity=".8"/>
    <path d="M430 1000 C520 980 600 960 680 975 C760 990 830 960 880 930 V790 C820 800 770 780 700 790 C600 800 520 770 450 800 Z" fill="var(--white)" opacity=".85"/>
    <path d="M0 780 C200 760 300 720 460 780 C600 830 740 760 880 700" fill="none" stroke="#d9e8c0" stroke-width="1.5"/>
  </svg>

  <div class="abs brand">Maplecrest Dental Care</div>
  <div class="abs intro">Introducing</div>
  <h1 class="abs headline">SMILE CLUB</h1>
  <div class="abs subhead">MEMBERSHIP</div>
  <p class="abs tagline">AFFORDABLE DENTAL CARE - <strong>NO INSURANCE REQUIRED</strong></p>

  <section class="plan plan--core">
    <div class="ribbon"><span class="ribbon__name">CORE CARE</span><span class="ribbon__type">PREVENTIVE</span></div>
    <div class="price"><sup>$</sup><b>39</b><small>/MONTH</small></div>
    <ul class="features">
      <li><svg class="tick" viewBox="0 0 14 14"><circle cx="7" cy="7" r="6" fill="none" stroke="currentColor"/><path d="M4 7.2l2 2 4-4.4" fill="none" stroke="currentColor" stroke-width="1.3"/></svg>Comprehensive Annual Exam</li>
      <li><svg class="tick" viewBox="0 0 14 14"><circle cx="7" cy="7" r="6" fill="none" stroke="currentColor"/><path d="M4 7.2l2 2 4-4.4" fill="none" stroke="currentColor" stroke-width="1.3"/></svg>2 Professional Cleanings per Year</li>
      <li><svg class="tick" viewBox="0 0 14 14"><circle cx="7" cy="7" r="6" fill="none" stroke="currentColor"/><path d="M4 7.2l2 2 4-4.4" fill="none" stroke="currentColor" stroke-width="1.3"/></svg>Routine Bitewing X-rays</li>
      <li><svg class="tick" viewBox="0 0 14 14"><circle cx="7" cy="7" r="6" fill="none" stroke="currentColor"/><path d="M4 7.2l2 2 4-4.4" fill="none" stroke="currentColor" stroke-width="1.3"/></svg>10% Savings on Treatment</li>
    </ul>
  </section>

  <section class="plan plan--bright">
    <div class="ribbon"><span class="ribbon__name">BRIGHT</span><span class="ribbon__type">COSMETIC</span></div>
    <div class="price"><sup>$</sup><b>59</b><small>/MONTH</small></div>
    <ul class="features">
      <li><svg class="tick" viewBox="0 0 14 14"><circle cx="7" cy="7" r="6" fill="none" stroke="currentColor"/><path d="M4 7.2l2 2 4-4.4" fill="none" stroke="currentColor" stroke-width="1.3"/></svg>Annual In-Office Whitening (Top &amp; Bottom)</li>
      <li><svg class="tick" viewBox="0 0 14 14"><circle cx="7" cy="7" r="6" fill="none" stroke="currentColor"/><path d="M4 7.2l2 2 4-4.4" fill="none" stroke="currentColor" stroke-width="1.3"/></svg>Custom Whitening Trays</li>
      <li><svg class="tick" viewBox="0 0 14 14"><circle cx="7" cy="7" r="6" fill="none" stroke="currentColor"/><path d="M4 7.2l2 2 4-4.4" fill="none" stroke="currentColor" stroke-width="1.3"/></svg>15% Savings on Elective Treatment</li>
    </ul>
  </section>

  <section class="plan plan--total">
    <div class="ribbon"><span class="ribbon__name">TOTAL SMILE</span><span class="ribbon__type">PERIODONTAL</span></div>
    <div class="price"><sup>$</sup><b>89</b><small>/MONTH</small></div>
    <ul class="features">
      <li><svg class="tick" viewBox="0 0 14 14"><circle cx="7" cy="7" r="6" fill="none" stroke="currentColor"/><path d="M4 7.2l2 2 4-4.4" fill="none" stroke="currentColor" stroke-width="1.3"/></svg>3-4 Perio Maintenance Visits per Year</li>
      <li><svg class="tick" viewBox="0 0 14 14"><circle cx="7" cy="7" r="6" fill="none" stroke="currentColor"/><path d="M4 7.2l2 2 4-4.4" fill="none" stroke="currentColor" stroke-width="1.3"/></svg>1 Comprehensive Exam</li>
      <li><svg class="tick" viewBox="0 0 14 14"><circle cx="7" cy="7" r="6" fill="none" stroke="currentColor"/><path d="M4 7.2l2 2 4-4.4" fill="none" stroke="currentColor" stroke-width="1.3"/></svg>Diagnostic X-rays</li>
      <li><svg class="tick" viewBox="0 0 14 14"><circle cx="7" cy="7" r="6" fill="none" stroke="currentColor"/><path d="M4 7.2l2 2 4-4.4" fill="none" stroke="currentColor" stroke-width="1.3"/></svg>15% Savings on Restorative &amp; Elective Care</li>
    </ul>
  </section>

  <section class="package">
    <div class="ribbon"><span class="ribbon__name">SMILE</span><span class="ribbon__type">REFRESH PACKAGE</span></div>
    <div class="badge-new">NEW</div>
    <div class="package-price"><sup>$</sup><b>499</b></div>
    <ul class="features">
      <li><svg class="tick" viewBox="0 0 14 14"><circle cx="7" cy="7" r="6" fill="none" stroke="currentColor"/><path d="M4 7.2l2 2 4-4.4" fill="none" stroke="currentColor" stroke-width="1.3"/></svg>Cleaning + Comprehensive Exam + Whitening</li>
      <li><svg class="tick" viewBox="0 0 14 14"><circle cx="7" cy="7" r="6" fill="none" stroke="currentColor"/><path d="M4 7.2l2 2 4-4.4" fill="none" stroke="currentColor" stroke-width="1.3"/></svg>Limited Time Offer</li>
    </ul>
  </section>

  <section class="financing">
    <h2 class="financing__title">FLEXIBLE FINANCING FOR TREATMENT:</h2>
    <div class="partners">
      <span class="partner partner--a"><i></i>FlexPay</span>
      <span class="partner partner--b"><i></i>Plumline</span>
    </div>
    <p class="financing__note">PAYMENT PLANS AVAILABLE<span>$49 Lifetime Activation Fee</span><span>(Non-Refundable)</span></p>
  </section>

  <p class="abs cta">JOIN SMILE CLUB TODAY! 865-555-0142</p>
</main>
</body>
</html>
```